Business Card and Simple Logo Desgin

New Zealand based start up company "Brook Advisory LTD" requires business cards and simple logo design.

Card Content.

Brook Advisory LTD

Joanna Pritchard
CA, BMS (Hons)

j.pritchard@brookadvisory.co.nz
PH +64 21 574 160

Target Market(s)

Corporate Business in IT, Finance and accounting.

Industry/Entity Type

Business

```html
<!DOCTYPE html>
<html lang="en">
<head>
<meta charset="utf-8">
<title>Brook Advisory LTD — Business Card</title>
<link rel="stylesheet" href="https://fonts.googleapis.com/css2?family=Marcellus&family=EB+Garamond:wght@400&display=swap">
<style>
  :root {
    --page-bg: #ffffff;
    --card-light: #dcd8b4;
    --card-mid: #cfca9f;
    --card-dark: #bdb68a;
    --pattern-tone: #a9a37f;
    --ink: #23231c;
    --mark-line: #2e2d24;
  }
  * { margin: 0; padding: 0; box-sizing: border-box; }
  html, body {
    width: 1200px;
    height: 799px;
    overflow: hidden;
    background: var(--page-bg);
  }
  .canvas {
    position: relative;
    width: 1200px;
    height: 799px;
  }
  .business-card {
    position: absolute;
    left: 150px;
    top: 158px;
    width: 900px;
    height: 482px;
    background: linear-gradient(170deg, var(--card-light) 0%, var(--card-mid) 60%, var(--card-dark) 100%);
    box-shadow: 0 6px 24px rgba(0, 0, 0, 0.12);
    overflow: hidden;
    color: var(--ink);
  }
  .background-pattern {
    position: absolute;
    left: 230px;
    top: 0;
    width: 670px;
    height: 482px;
    background: radial-gradient(ellipse at 70% 40%, rgba(169, 163, 127, 0.55) 0%, rgba(169, 163, 127, 0.25) 45%, rgba(169, 163, 127, 0) 75%);
  }
  .company-name {
    position: absolute;
    left: 56px;
    top: 162px;
    font-family: "Marcellus", serif;
    font-size: 33px;
    letter-spacing: 0.5px;
  }
  .brand-mark {
    position: absolute;
    left: 520px;
    top: 92px;
    display: flex;
    align-items: center;
    gap: 18px;
  }
  .brand-mark__dot {
    width: 34px;
    height: 34px;
    border: 2px solid var(--mark-line);
    border-radius: 50%;
  }
  .brand-mark__name {
    font-family: "Marcellus", serif;
    font-size: 30px;
    color: var(--ink);
  }
  .person {
    position: absolute;
    left: 56px;
    top: 296px;
    font-family: "EB Garamond", serif;
  }
  .person__name {
    font-size: 30px;
    line-height: 1;
  }
  .person__credentials {
    font-size: 23px;
    line-height: 1.1;
    margin-top: 2px;
  }
  .contact {
    position: absolute;
    left: 56px;
    top: 396px;
    font-family: "EB Garamond", serif;
    font-size: 23px;
    line-height: 1.0;
  }
</style>
</head>
<body>
  <main class="canvas">
    <section class="business-card">
      <div class="background-pattern" role="img" aria-label="Faint large decorative pattern in soft khaki tones"></div>

      <h1 class="company-name">Brook Advisory LTD</h1>

      <div class="brand-mark">
        <span class="brand-mark__dot"></span>
        <span class="brand-mark__name">Brook Advisory</span>
      </div>

      <div class="person">
        <p class="person__name">Joanna Pritchard</p>
        <p class="person__credentials">CA, BMS (Hons)</p>
      </div>

      <div class="contact">
        <p class="contact__email">j.pritchard@brookadvisory.co.nz</p>
        <p class="contact__phone">PH +64 21 574 160</p>
      </div>
    </section>
  </main>
</body>
</html>
```